RONEK PIPE SYSTEMS

Wrap designed for truck using ronek pipe logo colours, have yellow, blue, green water drops and hydraulics hoses. More colour.

Requirements
Must have
• Wrap designed for truck using ronek pipe logo colours, have yellow, blue, green water drops and hydraulics hoses. More colour.
Nice to have

```html
<!DOCTYPE html>
<html lang="en">
<head>
<meta charset="utf-8">
<title>Ronek Pipe Systems – Truck Wrap</title>
<link rel="stylesheet" href="https://fonts.googleapis.com/css2?family=Roboto+Condensed:wght@700;800&family=Exo+2:ital,wght@1,800&display=swap">
<style>
  :root {
    --navy: #272c7a;
    --green: #4b9f4a;
    --white: #f7f8f8;
    --steel-light: #e4e6e8;
    --steel-dark: #8d9298;
    --backdrop: #eef0f2;
  }
  html, body {
    margin: 0;
    padding: 0;
    width: 769px;
    height: 1200px;
    overflow: hidden;
    background: var(--backdrop);
  }
  .canvas {
    position: relative;
    width: 769px;
    height: 1200px;
  }
  .panel {
    position: absolute;
    overflow: hidden;
    background: var(--white);
    box-shadow: 0 2px 8px rgba(0,0,0,.12);
  }
  .panel svg.artwork {
    position: absolute;
    inset: 0;
  }
  .side-panel { left: 34px; top: 40px; width: 700px; height: 333px; }
  .rear-panel { left: 80px; top: 410px; width: 610px; height: 528px; background: var(--navy); }
  .hose-photo { position: absolute; }
  .brand-name {
    position: absolute;
    margin: 0;
    text-align: center;
    color: var(--navy);
    font-family: "Roboto Condensed", sans-serif;
    font-weight: 800;
    line-height: 1.02;
    letter-spacing: .5px;
  }
  .services {
    position: absolute;
    margin: 0;
    text-align: center;
    color: var(--navy);
    font-family: "Roboto Condensed", sans-serif;
    font-weight: 700;
    white-space: nowrap;
  }
  .brand-dot {
    position: absolute;
    border-radius: 50%;
    background: var(--green);
  }
  .phone, .website {
    position: absolute;
    margin: 0;
    color: var(--white);
    font-family: "Exo 2", sans-serif;
    font-style: italic;
    font-weight: 800;
    white-space: nowrap;
  }
  .website { text-transform: uppercase; }

  /* side panel text */
  .side-panel .brand-dot { left: 162px; top: 70px; width: 38px; height: 38px; }
  .side-panel .brand-name { left: 40px; top: 120px; width: 282px; font-size: 46px; }
  .side-panel .services { left: 40px; top: 266px; width: 282px; font-size: 13px; }
  .side-panel .phone { left: 355px; top: 252px; font-size: 26px; }
  .side-panel .website { left: 378px; top: 286px; font-size: 15px; }

  /* rear panel text */
  .rear-panel .brand-dot { left: 277px; top: 80px; width: 56px; height: 56px; }
  .rear-panel .brand-name { left: 120px; top: 160px; width: 370px; font-size: 58px; }
  .rear-panel .services { left: 120px; top: 318px; width: 370px; font-size: 15.5px; }
  .rear-panel .phone { left: 162px; top: 382px; font-size: 34px; }
  .rear-panel .website { left: 195px; top: 428px; font-size: 20px; }
</style>
</head>
<body>
<main class="canvas">

  <!-- Side box wrap -->
  <section class="panel side-panel" aria-label="Truck side panel wrap">
    <svg class="artwork" width="700" height="333" viewBox="0 0 700 333">
      <rect x="0" y="0" width="700" height="13" fill="var(--navy)"/>
      <polygon points="0,40 60,13 90,13 0,75" fill="var(--navy)"/>
      <polygon points="0,100 70,30 700,30 700,36 78,36 0,115" fill="var(--green)"/>
      <polygon points="0,125 80,43 700,43 700,50 88,50 0,138" fill="var(--navy)" opacity="0"/>
      <polygon points="405,48 450,48 610,254 565,254" fill="var(--green)"/>
      <polygon points="330,254 700,254 700,311 310,311" fill="var(--navy)"/>
      <rect x="0" y="299" width="700" height="15" fill="var(--navy)"/>
      <rect x="0" y="314" width="700" height="19" fill="var(--green)"/>
      <polygon points="600,254 640,254 700,320 700,333 660,333" fill="var(--green)"/>
    </svg>
    <svg class="hose-photo" style="left:440px;top:40px" width="260" height="220" viewBox="0 0 260 220"
         role="img" aria-label="Photo of chrome hydraulic hose fittings">
      <defs>
        <linearGradient id="steelSide" x1="0" y1="0" x2="1" y2="1">
          <stop offset="0" stop-color="var(--steel-light)"/>
          <stop offset="1" stop-color="var(--steel-dark)"/>
        </linearGradient>
      </defs>
      <polygon points="0,20 70,0 260,0 260,220 200,220" fill="url(#steelSide)"/>
    </svg>
    <span class="brand-dot"></span>
    <h1 class="brand-name">RONEK PIPE<br>SYSTEMS</h1>
    <p class="services">FUEL - AIR - WATER - OIL - GREASE</p>
    <p class="phone">123-456-7890</p>
    <p class="website">clinet website.com</p>
  </section>

  <!-- Rear doors wrap -->
  <section class="panel rear-panel" aria-label="Truck rear doors wrap">
    <svg class="artwork" width="610" height="528" viewBox="0 0 610 528">
      <polygon points="0,340 100,36 150,36 25,400" fill="var(--green)"/>
      <polygon points="610,340 510,36 460,36 585,400" fill="var(--green)"/>
      <path d="M219,36 H391 L585,400 Q595,420 575,420 L580,466 H19 L30,420 Q15,420 25,400 Z" fill="var(--white)"/>
      <path d="M30,390 L130,90 L150,90 L50,390 Q45,400 30,390 Z" fill="var(--green)" opacity="0"/>
      <path d="M127,466 V400 Q127,363 165,363 H470 Q507,363 507,400 V466 Z" fill="var(--green)"/>
      <rect x="0" y="466" width="610" height="12" fill="var(--green)"/>
      <rect x="0" y="478" width="610" height="50" fill="var(--navy)"/>
    </svg>
    <svg class="hose-photo" style="left:0;top:0" width="210" height="360" viewBox="0 0 210 360"
         role="img" aria-label="Photo of chrome hydraulic hose fittings">
      <defs>
        <linearGradient id="steelRearL" x1="1" y1="0" x2="0" y2="1">
          <stop offset="0" stop-color="var(--steel-light)"/>
          <stop offset="1" stop-color="var(--steel-dark)"/>
        </linearGradient>
      </defs>
      <polygon points="0,0 180,0 210,170 70,170 0,360" fill="url(#steelRearL)"/>
    </svg>
    <svg class="hose-photo" style="left:400px;top:0" width="210" height="360" viewBox="0 0 210 360"
         role="img" aria-label="Photo of chrome hydraulic hose fittings">
      <defs>
        <linearGradient id="steelRearR" x1="0" y1="0" x2="1" y2="1">
          <stop offset="0" stop-color="var(--steel-light)"/>
          <stop offset="1" stop-color="var(--steel-dark)"/>
        </linearGradient>
      </defs>
      <polygon points="210,0 30,0 0,170 140,170 210,360" fill="url(#steelRearR)"/>
    </svg>
    <span class="brand-dot"></span>
    <h2 class="brand-name">RONEK PIPE<br>SYSTEMS</h2>
    <p class="services">FUEL - AIR - WATER - OIL - GREASE</p>
    <p class="phone">123-456-7890</p>
    <p class="website">clinet website.com</p>
  </section>

</main>
</body>
</html>
```